Business Card Design - Trelvo Services

Trelvo Services is a service company which carried out installation and maintenance work in the GPS Tracking industry.

We install and maintain GPS Tracking hardware into cars, trucks etc.

We have an existing design with existing logo which I would like to improve on. I would like to be able to edit the design in the future when we have new staff come on board. We currently have 8 or so different employees who would all require cards - ideally I need to be able to edit a template in photoshop or something.

The back of the existing design has a white outline of Australia with a white dot over: Brisbane, Sydney, Melbourne, Adelaide and Perth.

Our current cards are mainly black, our uniforms are black - happy to look at changing that if the look is right.

We strive to be organised, professional and we are working in the technology sector.

Cheers.

Industry/Entity Type

Business

Contact Information for Business Card

Name
Mobile number
Email address
Web address

Requirements
Must have
• Map of Australia as mentioned above.

```html
<!DOCTYPE html>
<html lang="en">
<head>
<meta charset="utf-8">
<title>Trelvo Services – Business Card</title>
<link rel="stylesheet" href="https://fonts.googleapis.com/css2?family=Arimo:wght@400&family=Saira+Semi+Condensed:wght@700&display=swap">
<style>
  :root {
    --card-blue: #579dd5;
    --map-blue: #4a89be;
    --map-edge: #5a9ed4;
    --brand-dark: #2b2b2b;
    --accent-lime: #cddc3a;
    --name-white: #ffffff;
  }
  html, body {
    margin: 0;
    padding: 0;
    width: 1200px;
    height: 741px;
    overflow: hidden;
    background: var(--card-blue);
  }
  .card {
    position: relative;
    width: 1200px;
    height: 741px;
    background: var(--card-blue);
    overflow: hidden;
    font-family: "Arimo", Arial, sans-serif;
  }
  .australia-map {
    position: absolute;
    left: 70px;
    top: 0;
    width: 1010px;
    height: 741px;
    background: radial-gradient(ellipse at 45% 55%, var(--map-blue) 0%, var(--map-blue) 45%, var(--map-edge) 75%, var(--card-blue) 100%);
    border-radius: 42% 38% 40% 48% / 30% 34% 46% 52%;
    opacity: 0.75;
  }
  .brand-name {
    position: absolute;
    left: 70px;
    top: 78px;
    margin: 0;
    font-family: "Saira Semi Condensed", "Arial Narrow", sans-serif;
    font-weight: 700;
    font-size: 66px;
    line-height: 1;
    letter-spacing: -1px;
    color: var(--brand-dark);
  }
  .staff-name {
    position: absolute;
    left: 499px;
    top: 247px;
    margin: 0;
    font-size: 55px;
    font-weight: 400;
    line-height: 1;
    color: var(--name-white);
  }
  .name-rule {
    position: absolute;
    left: 503px;
    top: 321px;
    width: 646px;
    height: 8px;
    background: var(--accent-lime);
  }
  .contact-list {
    list-style: none;
    margin: 0;
    padding: 0;
  }
  .contact-item {
    position: absolute;
    margin: 0;
    font-size: 50px;
    line-height: 1;
    color: var(--accent-lime);
  }
  .contact-mobile  { left: 498px; top: 382px; }
  .contact-email   { left: 495px; top: 460px; }
  .contact-website { left: 494px; top: 540px; }
  .contact-address { left: 493px; top: 622px; }
</style>
</head>
<body>
  <main class="card">
    <div class="australia-map" role="img" aria-label="Hand-drawn outline map of Australia with state borders, in darker blue"></div>

    <h1 class="brand-name">Trelvo Services</h1>

    <p class="staff-name">Name</p>
    <div class="name-rule"></div>

    <ul class="contact-list">
      <li class="contact-item contact-mobile">Mobile #</li>
      <li class="contact-item contact-email">Email</li>
      <li class="contact-item contact-website">Website</li>
      <li class="contact-item contact-address">Address</li>
    </ul>
  </main>
</body>
</html>
```